Fresh & Clean *NEW* BUSINESS CARD Needed - OPTOMETRY Clinic/Optical

High-tech optometry practice with 3 doctors seeking new business card.  We provide eye exams, sell, designer glasses/contacts/specialty eyewear and treat ocular diseases.  For our business cards, we are seeking fresh, clean, and crisp design as we grow our team (staffing change).  Simply adding doctors is making the card look busy/cluttered.
 Looking for professional, less cluttered look yet still have our logo, doctor names, phone, address, and website....If possible!  :)
Names:
Marcia Trelford, O.D.
Ned Pallister, O.D.
Oona Ferrant, O.D.
Phone: 555-014-2738
Website: www.BrightLensHub.example
Address:  417 Garnet R. Holloway, Alderbrook, ST 00000
Ultimately we have the main business card with all doctor sames and that card has two versions  (front is always the same).  The back has two designs (1) displays next appointment time/date, (2) for "general use" (non-appointment.)    I have attached what we have used in the past.  
We also need a design template for each team member in our practice with their name, title, and email.   Those should be designed with the "general use" back (see attached).
**Open to entirely new design so don't feel obligated to keep current format.  Need new perspective!  Also including our watermark and some other design features we have consistently used in past in our portfolio.  Included are two options for logos--vertical and horizontal.
**I also would like to remove "Member of Sight Alliance" on our logo if possible**
 Other image files available upon request.

Target Market(s)

New patient & Current Patients

Industry/Entity Type

Optometry

Contact Information for Business Card

High-tech optometry practice with 3 doctors seeking new business card.  We provide eye exams, sell, designer glasses/contacts/specialty eyewear and treat ocular diseases.  For our business cards, we are seeking fresh, clean, and crisp design as we grow our team (staffing change).  Simply adding doctors is making the card look busy/cluttered.  Looking for professional, less cluttered look yet still have our logo, doctor names, phone, address, and website....If possible!  :) Names: Marcia Trelford, O.D. Ned Pallister, O.D. Oona Ferrant, O.D. Phone: 555-014-2738 Website: www.BrightLensHub.example Address:  417 Garnet R. Holloway, Alderbrook, ST 00000 Ultimately we have the main business card with all doctor sames and that card has two versions  (front is always the same).  The back has two designs (1) displays next appointment time/date, (2) for "general use" (non-appointment.)    I have attached what we have used in the past.   We also need a design template for each team member in our practice with their name, title, and email.   Those should be designed with the "general use" back (see attached). **Open to entirely new design so don't feel obligated to keep current format.  Need new perspective!  Also including our watermark and some other design features we have consistently used in past in our portfolio.  Included are two options for logos--vertical and horizontal. **I also would like to remove "Member of Sight Alliance" on our logo if possible**  Other image files available upon request.

Font styles to use
Other font styles liked:
• We have used Montserrat / Yellowtail in the past

Colors

Designer to choose colors to be used in the design.

Requirements
Must have
• Clean & Fresh Design with Logo / Info provided in description. Horizontal orientation. **I have included the CMYK colors we currently have in our logo.
Should not have
• Cluttered

```html
<!DOCTYPE html>
<html lang="en">
<head>
<meta charset="utf-8">
<title>Bright Lens Hub – Business Cards</title>
<link rel="stylesheet" href="https://fonts.googleapis.com/css2?family=Montserrat:wght@300;400;500;700;800&display=swap">
<style>
  :root{
    --bg:#2c2c2e;
    --paper:#ffffff;
    --ink:#111111;
    --brand-grey:#6f7072;
    --panel-grey:#707173;
    --sky:#a9dce6;
    --slate:#2f3b45;
    --olive:#6e6a10;
    --amber:#8a5a10;
    --cocoa:#2a0e05;
    --gold:#d6a71f;
  }
  *{box-sizing:border-box;margin:0;padding:0}
  html,body{width:1200px;height:875px;overflow:hidden}
  body{background:var(--bg);font-family:"Montserrat",sans-serif;position:relative}

  .card{position:absolute;width:540px;height:310px;border-radius:18px;overflow:hidden;background:var(--paper)}
  .card--appointment{left:40px;top:140px}
  .card--info{left:620px;top:425px}

  /* colour bands */
  .band{position:absolute;left:0;right:0;height:12px;display:flex}
  .band--top{top:0}
  .band--bottom{bottom:0;flex-direction:row-reverse}
  .band span{flex:1}
  .band .c1{background:var(--slate)}
  .band .c2{background:var(--sky)}
  .band .c3{background:var(--olive)}
  .band .c4{background:var(--amber)}
  .band .c5{background:var(--cocoa)}

  .brand{position:absolute;display:flex;align-items:center;gap:12px}
  .brand__dot{width:34px;height:34px;border-radius:50%;background:var(--sky);flex:none}
  .brand__name{font-weight:300;color:var(--brand-grey);font-size:38px;letter-spacing:.5px;line-height:1}

  .card--appointment .brand{left:32px;top:42px}
  .watermark{position:absolute;left:150px;top:60px;width:220px;height:220px;border-radius:50%;border:22px solid #ececec;opacity:.8}
  .appt__title{position:absolute;left:92px;top:110px;font-weight:800;font-size:19px;color:var(--ink)}
  .appt__fields{position:absolute;left:40px;right:40px;top:160px;display:flex;gap:14px;font-size:15px;font-weight:400;color:var(--ink)}
  .appt__field{flex:1;display:flex;align-items:flex-end}
  .appt__field i{flex:1;border-bottom:2px dotted var(--ink);margin-left:4px;height:14px}
  .appt__notice{position:absolute;left:30px;right:30px;top:208px;text-align:center;font-weight:800;font-size:17px;line-height:1.35;color:var(--ink)}

  .card--info .brand{left:28px;top:38px}
  .info__panel{position:absolute;left:0;right:0;top:118px;bottom:0;background:var(--panel-grey)}
  .info__ring{position:absolute;right:28px;top:40px;width:190px;height:190px;border-radius:50%;background:var(--sky);border:12px solid var(--paper)}
  .doctors{position:absolute;left:28px;top:134px;color:var(--paper);font-weight:800;font-size:18px;line-height:1.3}
  .contacts{position:absolute;left:28px;top:218px;color:var(--paper);font-weight:400;font-size:12.5px;line-height:1.5;list-style:none}
  .contacts li{display:flex;align-items:flex-start;gap:8px}
  .contacts svg{width:12px;height:12px;flex:none;margin-top:3px;fill:var(--gold)}
</style>
</head>
<body>

<section class="card card--appointment" aria-label="Appointment card back">
  <div class="band band--top"><span class="c1"></span><span class="c2"></span><span class="c3"></span><span class="c4"></span><span class="c5"></span></div>
  <div class="watermark" aria-hidden="true"></div>
  <div class="brand"><span class="brand__dot"></span><span class="brand__name">brightlenshub</span></div>
  <h2 class="appt__title">Your Next Appointment</h2>
  <div class="appt__fields">
    <div class="appt__field">Date<i></i></div>
    <div class="appt__field">Time<i></i></div>
  </div>
  <p class="appt__notice">If you unable to keep your appointment<br>kindly give us 24 hour notice</p>
  <div class="band band--bottom"><span class="c1"></span><span class="c2"></span><span class="c3"></span><span class="c4"></span><span class="c5"></span></div>
</section>

<section class="card card--info" aria-label="Practice card front">
  <div class="info__panel"></div>
  <div class="info__ring" aria-hidden="true"></div>
  <div class="brand"><span class="brand__dot"></span><span class="brand__name">brightlenshub</span></div>
  <div class="doctors">
    <p>Marcia Trelford, O.D.</p>
    <p>Ned Pallister, O.D.</p>
    <p>Oona Ferrant, O.D.</p>
  </div>
  <ul class="contacts">
    <li><svg viewBox="0 0 24 24"><path d="M6.6 10.8a15 15 0 0 0 6.6 6.6l2.2-2.2a1 1 0 0 1 1-.25 11.4 11.4 0 0 0 3.6.57 1 1 0 0 1 1 1V20a1 1 0 0 1-1 1A17 17 0 0 1 3 4a1 1 0 0 1 1-1h3.5a1 1 0 0 1 1 1c0 1.250.2 2.450.57 3.6a1 1 0 0 1-.25 1z"/></svg>555-014-2738</li>
    <li><svg viewBox="0 0 24 24"><path d="M12 2a10 10 0 1 0 0 20 10 10 0 0 0 0-20zm6.9 6h-2.9a15.7 15.7 0 0 0-1.4-3.6A8 8 0 0 1 18.9 8zM12 4c.8 1.2 1.5 2.5 1.9 4h-3.8c.4-1.5 1.1-2.8 1.9-4zM4.3 14a8 8 0 0 1 0-4h3.4a16 16 0 0 0 0 4zm.8 2h2.9c.3 1.3.8 2.5 1.4 3.6A8 8 0 0 1 5.1 16zM8 8H5.1a8 8 0 0 1 4.3-3.6C8.8 5.5 8.4 6.7 8 8zm4 12c-.8-1.2-1.5-2.5-1.9-4h3.8c-.4 1.5-1.1 2.8-1.9 4zm2.3-6H9.7a14.7 14.7 0 0 1 0-4h4.6a14.7 14.7 0 0 1 0 4zm.3 5.6c.6-1.1 1.1-2.3 1.4-3.6h2.9a8 8 0 0 1-4.3 3.6zm1.7-5.6a16 16 0 0 0 0-4h3.4a8 8 0 0 1 0 4z"/></svg>www.BrightLensHub.example</li>
    <li><svg viewBox="0 0 24 24"><path d="M12 2a7 7 0 0 0-7 7c0 5.2 7 13 7 13s7-7.8 7-13a7 7 0 0 0-7-7zm0 9.5a2.5 2.5 0 1 1 0-5 2.5 2.5 0 0 1 0 5z"/></svg><span>417 Garnet R. Holloway,<br>Alderbrook, ST 00000</span></li>
  </ul>
</section>

</body>
</html>
```